Elevated Kinetic Framework

I am a competitive bodybuilder marketing my articles and videos. I envision a picture of my physique that allows the user to click on different body parts to receive three options: free article, fee based video or fee based personalized routine. I also need a page describing meal planning options that includes videos. Would also like pages for photos and blogging.
I want to maximize site visibility. Many fitness sites use what appears to be a template like this: http://www.marlowtpeck.example/Build-7-8-Kilos-Of-Lean-Tissue.html. I would be interested in incorporating some pages like that.

I have a current site at corbinlusk.example. I have not created video content yet.I can provide my current hosting details if needed. Feel free to contact me to discuss any design questions at corbin@lusk.example or 555 614 8297.

Target Market(s)

health and fitness, weight loss, muscle gain, body building, power lifting, wellness, natural medicine

Industry/Entity Type

Marketing

Requirements
Must have
• I can provide full body photos. Want my business and personal name displayed. Possible flash design that starts small then quickly increases in size on main page?

```html
<!DOCTYPE html>
<html lang="en">
<head>
<meta charset="utf-8">
<title>Corbin Lusk – Truth in Bodybuilding</title>
<link href="https://fonts.googleapis.com/css2?family=PT+Sans+Narrow:wght@400;700&family=Source+Sans+3:wght@400;600&family=Titillium+Web:wght@700&display=swap" rel="stylesheet">
<style>
  :root{
    --brand:#0d4c74;
    --footer:#0e4a72;
    --ink:#333;
    --muted:#555;
    --panel:#efefef;
    --line:#e2e2e2;
    --white:#fff;
  }
  *{box-sizing:border-box;margin:0;padding:0}
  html,body{width:924px;height:1200px;overflow:hidden;background:var(--white)}
  body{position:relative;font-family:"Source Sans 3",sans-serif;color:var(--ink)}
  .abs{position:absolute}

  .brand{left:95px;top:50px}
  .brand-name{font-family:"Titillium Web",sans-serif;font-weight:700;font-size:29px;color:var(--brand);letter-spacing:.5px;line-height:1}
  .brand-tag{font-size:9.5px;letter-spacing:6.3px;color:var(--ink);margin-top:3px}

  .search{left:700px;top:42px;width:132px;height:19px;border-radius:9px;background:var(--panel);font-size:8px;color:#aaa;padding:3px 6px}
  .search svg{position:absolute;right:7px;top:5px}

  .main-nav{right:92px;top:71px;font-family:"PT Sans Narrow",sans-serif;font-size:17px;color:var(--ink);display:flex;gap:7px}
  .main-nav span.sep{color:var(--ink)}

  .hero{left:92px;top:111px;width:740px;height:352px;display:flex}
  .hero-shot{height:100%}
  .shot-1{width:242px;background:linear-gradient(180deg,#4f6b3a 0%,#6e8a3c 40%,#4d7a2a 100%)}
  .shot-2{width:232px;background:linear-gradient(180deg,#2f3a26 0%,#6a3a22 45%,#3f6a25 100%)}
  .shot-3{width:266px;background:linear-gradient(180deg,#51693a 0%,#6d8c3e 40%,#4f7b2c 100%)}
  .hero-dots{right:14px;bottom:10px;display:flex;gap:3px}
  .hero-dots i{width:11px;height:11px;border-radius:50%;background:var(--white)}
  .hero-dots i.on{background:#1a7ec2}

  .section-title{font-family:"PT Sans Narrow",sans-serif;font-size:19px;color:var(--ink);font-weight:400}

  .about-photo{left:100px;top:517px;width:162px;height:233px;background:linear-gradient(160deg,#e9c98a,#c98a4e 60%,#a8683a)}
  .about-text{left:270px;top:514px;width:308px;font-size:10.4px;line-height:18.5px;color:var(--muted);text-align:justify}
  .about-text p+p{margin-top:18.5px}

  .contact{left:593px;top:517px;width:231px;height:232px;background:var(--panel)}
  .field{position:absolute;left:15px;width:202px;background:var(--white);border-radius:3px;font-size:10px;color:#999;padding:8px 10px}
  .send{position:absolute;left:65px;top:193px;width:93px;height:28px;background:var(--brand);color:var(--white);font-size:13px;text-align:center;line-height:28px;border-radius:2px;letter-spacing:.5px}

  .arrows{display:flex;gap:4px}
  .arrows svg{display:block}

  .thumb{width:231px;height:110px}
  .thumb-article{background:linear-gradient(160deg,#e8c088,#b8713e 55%,#8e5028);display:flex;align-items:center;justify-content:center}
  .thumb-workout{background:linear-gradient(180deg,#0c0c0c,#2a1a10 50%,#0c0c0c)}
  .gallery-photo{width:231px;height:293px;background:linear-gradient(180deg,#cfcac2,#b58766 40%,#8d5e44 75%,#3a2a22)}

  .card-title{font-family:"PT Sans Narrow",sans-serif;font-size:13px;color:var(--ink)}
  .card-meta{font-family:"PT Sans Narrow",sans-serif;font-size:13px;color:var(--ink)}
  .card-meta b{font-weight:400;color:var(--brand)}
  .card-body{font-family:"PT Sans Narrow",sans-serif;font-size:9.3px;line-height:18.5px;color:var(--muted);text-align:justify}
  .price{font-family:"PT Sans Narrow",sans-serif;font-weight:700;font-size:36px;color:var(--brand);line-height:1}
  .buy{background:var(--brand);color:var(--white);font-size:10px;font-weight:600;width:68px;height:20px;line-height:20px;text-align:center}

  .site-footer{left:0;top:1137px;width:924px;height:63px;background:var(--footer);color:var(--white)}
  .footer-nav{left:100px;top:12px;font-family:"PT Sans Narrow",sans-serif;font-size:10.5px;display:flex;gap:7px}
  .copyright{left:102px;top:37px;font-size:11px}
  .social{top:8px;display:flex;flex-direction:column;align-items:center;width:50px}
  .social i{width:30px;height:30px;border-radius:50%;background:#5aa9d6;border:2px solid #d8e8f2}
  .social span{font-size:7.5px;color:#cfe0ec;margin-top:4px}
</style>
</head>
<body>

<header>
  <div class="abs brand">
    <div class="brand-name">CORBIN LUSK</div>
    <div class="brand-tag">TRUTH IN BODYBUILDING</div>
  </div>
  <div class="abs search">Search
    <svg width="9" height="9" viewBox="0 0 9 9"><circle cx="3.8" cy="3.8" r="2.8" fill="none" stroke="#fff" stroke-width="1.2"/><line x1="6" y1="6" x2="8.5" y2="8.5" stroke="#fff" stroke-width="1.2"/></svg>
  </div>
  <nav class="abs main-nav">
    <span>About&nbsp; Me</span><span class="sep">&nbsp;|</span><span>Articles</span><span class="sep">|</span><span>Work Outs</span><span class="sep">|</span><span>Videos</span><span class="sep">|</span><span>Contact Us</span>
  </nav>
</header>

<section class="abs hero">
  <div class="hero-shot shot-1" role="img" aria-label="Bodybuilder posing front double biceps on a lawn"></div>
  <div class="hero-shot shot-2" role="img" aria-label="Bodybuilder close-up front pose on a lawn"></div>
  <div class="hero-shot shot-3" role="img" aria-label="Bodybuilder posing back double biceps on a lawn"></div>
  <div class="abs hero-dots"><i class="on"></i><i></i><i></i><i></i></div>
</section>

<h2 class="abs section-title" style="left:100px;top:478px">What this site is about...</h2>
<div class="abs about-photo" role="img" aria-label="Bodybuilder side chest pose against a warm wall"></div>
<div class="abs about-text">
  <p>As a lifelong veteran of competitive bodybuilding and powerlifting, I have learned the hard way that these sports are teeming with misinformation, lies and general dishonesty. The knowledge needed to build a body to its genetic maximum without the use of drugs is very difficult to obtain. I have dedicated my life to the pursuit of this knowledge and now that I have acquired it, I feel it is my obligation to make it available to everyone. This site can allow anyone to achieve their goals without fruitless efforts, injuries and wasted money. I have committed all these errors; now let me show you how to avoid them. Make no mistake, I am no guru, genius or expert.</p>
  <p>What I have done is simply compiled all of the truth regarding actual bodybuilding and made it available in one place.</p>
</div>

<h2 class="abs section-title" style="left:593px;top:478px">Quick Contact</h2>
<form class="abs contact">
  <div class="field" style="top:17px;height:30px">Username</div>
  <div class="field" style="top:54px;height:30px">E-mail Address</div>
  <div class="field" style="top:93px;height:84px">Message</div>
  <div class="send">SEND</div>
</form>

<!-- Articles -->
<h2 class="abs section-title" style="left:100px;top:779px">Articles for sale</h2>
<div class="abs arrows" style="left:294px;top:785px">
  <svg width="16" height="16" viewBox="0 0 16 16"><circle cx="8" cy="8" r="8" fill="var(--brand)"/><path d="M9.5 4.5 6 8l3.5 3.5" fill="none" stroke="#fff" stroke-width="2"/></svg>
  <svg width="16" height="16" viewBox="0 0 16 16"><circle cx="8" cy="8" r="8" fill="var(--brand)"/><path d="M6.5 4.5 10 8l-3.5 3.5" fill="none" stroke="#fff" stroke-width="2"/></svg>
</div>
<div class="abs thumb thumb-article" style="left:100px;top:817px" role="img" aria-label="Video thumbnail of abdominal muscles">
  <svg width="36" height="42" viewBox="0 0 36 42"><path d="M2 2 34 21 2 40Z" fill="#fff" opacity=".9"/></svg>
</div>
<div class="abs card-title" style="left:100px;top:938px">The Jewel of the Crown</div>
<div class="abs card-meta" style="left:100px;top:957px">Posted by , <b>Corbin Lusk , May 2013 22 nd</b></div>
<p class="abs card-body" style="left:100px;top:995px;width:231px">Abdominals are the visual centerpiece of the body. They tell everyone immediately what condition you are in. They demand respect unlike any other bodypart because they convey your discipline outside of the gym. Whether it is right or not, the public respects a 150 pound person with defined abs more than the 250 pound monster who hides his behind a tank top. And abs are even more crucial for competitors.</p>

<!-- Work Outs -->
<h2 class="abs section-title" style="left:346px;top:779px">Work Outs</h2>
<div class="abs arrows" style="left:541px;top:785px">
  <svg width="16" height="16" viewBox="0 0 16 16"><circle cx="8" cy="8" r="8" fill="var(--brand)"/><path d="M9.5 4.5 6 8l3.5 3.5" fill="none" stroke="#fff" stroke-width="2"/></svg>
  <svg width="16" height="16" viewBox="0 0 16 16"><circle cx="8" cy="8" r="8" fill="var(--brand)"/><path d="M6.5 4.5 10 8l-3.5 3.5" fill="none" stroke="#fff" stroke-width="2"/></svg>
</div>
<div class="abs thumb thumb-workout" style="left:346px;top:817px" role="img" aria-label="Four competitors posing on a dark stage"></div>
<div class="abs card-title" style="left:347px;top:938px">Mass Building</div>
<div class="abs price" style="left:346px;top:956px">$ 100</div>
<div class="abs buy" style="left:437px;top:964px">BUY NOW</div>
<p class="abs card-body" style="left:347px;top:995px;width:231px">This routine represents the best method for adding drug free mass for trainees of all backgrounds. This program will result in the addition of not only symmetrical lean mass but also the strength and power prerequisite to such gains. This makes the program ideal for individuals in any sport, not just the iron games. In short, this is the best way to train to develop your body, period.</p>

<!-- Photo Gallery -->
<h2 class="abs section-title" style="left:593px;top:779px">Photo Gallery</h2>
<div class="abs arrows" style="left:789px;top:785px">
  <svg width="16" height="16" viewBox="0 0 16 16"><circle cx="8" cy="8" r="8" fill="var(--brand)"/><path d="M9.5 4.5 6 8l3.5 3.5" fill="none" stroke="#fff" stroke-width="2"/></svg>
  <svg width="16" height="16" viewBox="0 0 16 16"><circle cx="8" cy="8" r="8" fill="var(--brand)"/><path d="M6.5 4.5 10 8l-3.5 3.5" fill="none" stroke="#fff" stroke-width="2"/></svg>
</div>
<div class="abs gallery-photo" style="left:593px;top:817px" role="img" aria-label="Two athletes standing together indoors"></div>

<footer class="abs site-footer">
  <nav class="abs footer-nav">
    <span>About&nbsp; Me</span><span>|</span><span>Articles</span><span>|</span><span>Work Outs</span><span>|</span><span>Videos</span><span>|</span><span>Contact Us</span>
  </nav>
  <div class="abs copyright">©2013 Company Name, All Rights Reserved</div>
  <div class="abs social" style="left:673px"><i></i><span>Flitter</span></div>
  <div class="abs social" style="left:711px"><i style="background:#4d7fc0"></i><span>Friendwall</span></div>
  <div class="abs social" style="left:747px"><i style="background:#f0a531"></i><span>RSS</span></div>
  <div class="abs social" style="left:784px"><i style="background:#3f97c9"></i><span>WorkLink</span></div>
</footer>

</body>
</html>
```